Accounting Practice Business Card Design

I have a logo I am happy for you to use in the design of the Business Card.
You can edit and change colours as you please, I am not fixated on it.
I am looking for a modern and clean overall feel for the finished design.

The business is a small accounting practice who thrives on word of mouth referrals and this card will be given to all current and prospect clients.

Industry/Entity Type

Accountant

Contact Information for Business Card

Marcus Elwin
Level 5, 8 Corvale Ridge Road
ASHGROVE RISE VIC 3187
Phone: 9481 3057
Email: melwin@mrfaccountants.com.au
Web: www.mrfaccountants.com.au

Font styles to use
Serif
Sans Serif

Colors
0555a3
3277b5
85acd3
0393ce
33a6d7
85cae6
00a990
33b8a4
9bcb3c

Requirements
Must have
• "The end to your tax problems begin with us"
• "A referral from you is our greatest compliment"
Nice to have
• Modern clean professional

```html
<!DOCTYPE html>
<html lang="en">
<head>
<meta charset="utf-8">
<title>MRF Accountants – Business Card</title>
<link rel="stylesheet" href="https://fonts.googleapis.com/css2?family=Carlito&family=Montserrat:wght@600;700&family=Questrial&display=swap">
<style>
  :root {
    --brand-blue: #0b45f5;
    --brand-green: #35e87a;
    --brand-sky: #3bb4f7;
    --paper: #ffffff;
    --edge: #9a9a9a;
  }
  * { margin: 0; padding: 0; box-sizing: border-box; }
  html, body { width: 1200px; height: 1200px; overflow: hidden; background: var(--paper); }
  .canvas { position: relative; width: 1200px; height: 1200px; }

  .card {
    position: absolute;
    left: 169px;
    width: 851px;
    height: 474px;
    background: var(--paper);
    border: 1px solid var(--edge);
    overflow: hidden;
    color: var(--brand-blue);
  }
  .card--front { top: 58px; }
  .card--back { top: 694px; }

  .front-bands { position: absolute; inset: 0; width: 100%; height: 100%; }

  .wordmark {
    position: absolute;
    font-family: "Montserrat", sans-serif;
    font-weight: 700;
    color: var(--brand-blue);
    text-align: center;
    line-height: 1;
    letter-spacing: -1px;
  }
  .wordmark span { display: block; }
  .wordmark__main { font-size: 96px; }
  .wordmark__sub { font-size: 38px; margin-top: 8px; }
  .card--front .wordmark { left: 12px; top: 148px; width: 334px; }
  .card--back .wordmark { left: 0; right: 0; top: 282px; }
  .card--back .wordmark__main { font-size: 90px; }
  .card--back .wordmark__sub { font-size: 34px; }

  .person { position: absolute; left: 470px; width: 360px; top: 64px; text-align: center; }
  .person__name {
    font-family: "Montserrat", sans-serif;
    font-weight: 700;
    font-size: 40px;
    letter-spacing: -2px;
    line-height: 1;
    padding-left: 20px;
  }
  .person__role { font-family: "Questrial", sans-serif; font-size: 22px; margin-top: 8px; }

  .address {
    position: absolute; left: 455px; width: 380px; top: 170px;
    font-family: "Questrial", sans-serif; font-size: 22px; line-height: 32px; text-align: center;
  }

  .contacts {
    position: absolute; left: 433px; top: 268px;
    font-family: "Questrial", sans-serif; font-size: 22px; line-height: 37px;
    list-style: none;
  }
  .contacts b { font-family: "Montserrat", sans-serif; font-weight: 600; font-size: 20px; letter-spacing: -0.5px; margin-right: 6px; }

  .tagline {
    position: absolute; left: 384px; top: 430px; width: 466px;
    font-family: "Montserrat", sans-serif; font-weight: 600; font-size: 16px;
    letter-spacing: -0.7px; white-space: nowrap;
  }

  .thanks {
    position: absolute; left: 0; right: 0; top: 44px;
    font-family: "Carlito", sans-serif; font-size: 44px; line-height: 48px; text-align: center;
  }
  .thanks__close { margin-top: 58px; }
</style>
</head>
<body>
<div class="canvas">

  <section class="card card--front">
    <svg class="front-bands" viewBox="0 0 1064 592" preserveAspectRatio="none" aria-hidden="true">
      <polygon points="505,0 1064,0 1064,592 419,592" fill="var(--brand-green)"/>
      <polygon points="522,18 1064,18 1064,592 437,592" fill="var(--brand-blue)"/>
      <polygon points="536,41 1064,41 1064,592 455,592" fill="var(--brand-sky)"/>
      <polygon points="549,61 1064,61 1064,592 471,592" fill="var(--paper)"/>
    </svg>

    <div class="wordmark"><span class="wordmark__main">MRF</span><span class="wordmark__sub">ACCOUNTANTS</span></div>

    <div class="person">
      <h1 class="person__name">MARCUS ELWIN</h1>
      <p class="person__role">accountant</p>
    </div>

    <p class="address">Level 5, 8 Corvale Ridge Road<br>ASHGROVE RISE VIC 3187</p>

    <ul class="contacts">
      <li><b>Phone:</b>9481 3057</li>
      <li><b>Email:</b>melwin@mrfaccountants.com.au</li>
      <li><b>Web:</b>www.mrfaccountants.com.au</li>
    </ul>

    <p class="tagline">THE END TO YOUR TAX PROBLEMS BEGIN WITH US</p>
  </section>

  <section class="card card--back">
    <div class="thanks">
      <p>A referral from you is our<br>greatest compliment</p>
      <p class="thanks__close">Thank you for choosing us</p>
    </div>
    <div class="wordmark"><span class="wordmark__main">MRF</span><span class="wordmark__sub">ACCOUNTANTS</span></div>
  </section>

</div>
</body>
</html>
```